Dovamel Nutrition Supplement Jar

Label for jar. White label on a brown bottle jar.
Conservative look, should look like medicine.
Main Side:
Oak Harbor Clinics (smaller size) (with logo)
DOVAMEL 10mg (large size)
Doctor Formulated
Developed in Clinical Practice
60 Capsules
(I prefer the single color white label with dark brown letters. Please stay close to that design)
(For the back side, please use the multicolor set up)
(The whole Label should be one color - white with dark brown letters)
Please visit my site for more inspiration and feel: www.velmorine.example
The product will be brown jar listed on this site.
Can you please provide one version without the text "Oak Harbor Clinics & Logo".
Thank you.

Target Market(s)

Women, 34-59 years old

Industry/Entity Type

Nutrition

Requirements
Should not have
• Multicolors, leaves,

```html
<!DOCTYPE html>
<html lang="en">
<head>
<meta charset="utf-8">
<title>Dovamel 10 mg – Jar Label</title>
<link href="https://fonts.googleapis.com/css2?family=Montserrat:wght@400;500;700&display=swap" rel="stylesheet">
<style>
  :root {
    --page-bg: #ececec;
    --label-white: #ffffff;
    --label-white-shade: #f6f4f2;
    --ink-brown: #3a2519;
    --rule-brown: rgba(58, 37, 25, 0.85);
  }
  html, body {
    margin: 0;
    padding: 0;
    width: 1200px;
    height: 1200px;
    overflow: hidden;
    background: var(--page-bg);
    font-family: "Montserrat", sans-serif;
  }
  .label {
    position: absolute;
    left: 229px;
    top: 85px;
    width: 742px;
    height: 1030px;
    background: linear-gradient(90deg, var(--label-white-shade) 0%, var(--label-white) 45%, var(--label-white-shade) 100%);
    color: var(--ink-brown);
    box-shadow: 0 0 0 1px rgba(58, 37, 25, 0.08);
  }
  .product-title {
    position: absolute;
    left: 90px;
    top: 78px;
    width: 592px;
    margin: 0;
    white-space: nowrap;
    line-height: 1;
    display: flex;
    align-items: baseline;
  }
  .product-name {
    font-weight: 700;
    font-size: 74px;
    letter-spacing: 0.5px;
  }
  .product-strength {
    font-weight: 500;
    font-size: 54px;
    margin-left: 14px;
  }
  .product-strength .unit {
    font-size: 44px;
  }
  .title-rule {
    position: absolute;
    left: 90px;
    top: 181px;
    width: 592px;
    height: 2px;
    background: var(--rule-brown);
  }
  .tagline {
    position: absolute;
    left: 90px;
    top: 210px;
    margin: 0;
    font-size: 26px;
    font-weight: 400;
    letter-spacing: 3.5px;
  }
  .accent-bar {
    position: absolute;
    left: 84px;
    top: 575px;
    width: 5px;
    height: 290px;
    background: linear-gradient(180deg, var(--ink-brown) 0%, rgba(58, 37, 25, 0) 100%);
  }
  .benefits {
    position: absolute;
    left: 130px;
    top: 572px;
    width: 560px;
    font-size: 28px;
    line-height: 38px;
    font-weight: 400;
  }
  .benefits p {
    margin: 0 0 38px 0;
  }
  .clinical-note {
    position: absolute;
    left: 113px;
    top: 870px;
    margin: 0;
    font-size: 23px;
    font-weight: 400;
    letter-spacing: 0.3px;
    white-space: nowrap;
  }
  .footer-rule {
    position: absolute;
    left: 113px;
    top: 918px;
    width: 569px;
    height: 2px;
    background: var(--rule-brown);
  }
  .capsule-count {
    position: absolute;
    left: 113px;
    top: 950px;
    margin: 0;
    font-size: 28px;
    font-weight: 400;
    letter-spacing: 4px;
  }
  .footer-divider {
    position: absolute;
    left: 448px;
    top: 936px;
    width: 2px;
    height: 62px;
    background: var(--rule-brown);
  }
  .clinic-name {
    position: absolute;
    left: 470px;
    top: 955px;
    margin: 0;
    font-size: 22px;
    font-weight: 500;
    white-space: nowrap;
  }
</style>
</head>
<body>
  <main class="label">
    <h1 class="product-title">
      <span class="product-name">DOVAMEL</span><span class="product-strength">10 <span class="unit">MG</span></span>
    </h1>
    <div class="title-rule"></div>
    <p class="tagline">DOCTOR FORMULATED</p>

    <div class="accent-bar"></div>
    <div class="benefits">
      <p>In Synergy our ingredients act on Neuro-receptors and Reward System Pathways in the Brain.</p>
      <p>Reduce cravings and mechanisms of addiction, promote motivation and positive behavior.</p>
    </div>

    <p class="clinical-note">DEVELOPED THROUGH CLINICAL PRACTICE</p>
    <div class="footer-rule"></div>
    <p class="capsule-count">60 CAPSULE</p>
    <div class="footer-divider"></div>
    <p class="clinic-name">Oak Harbor Clinics</p>
  </main>
</body>
</html>
```